Vintage Style Soup Package Label

I make dry soup packages. I am looking for a label for my soups that shows Quality, Homemade Goodness. Easy, Delicious. My company is called Uncle Barnaby Pantry, But I want this soup line to be called "Thistle & Rye " All my product has a very Vintage Antique look.
I Love Typography. My 6 cup soups are packaged in a flat black bag.
my website is www.unclebarnabypantry.example. I have 15 different Flavours. Our motto is Simple Suppers, Every Day.
While creating the label if you wanted to use
Please use "Chicken Pot Pie" as your sample please and thanks.

Target Market(s)

I want to sell my soups to upscale Grocery and Specialty stores.

Font styles to use
Serif
Sans Serif
Other font styles liked:
• Castellar

Colors
6c449b
ec1f27
ffc214
9ccb3b
ffffff
f37122

Requirements
Must have
• NOTE: A place for weight needs to be on the label

My labels I print on are Vertical 3.33 x4"
Colours. I do not like Pink or Pastel colours. I prefer Dark or grunge colours.
Nice to have
• NOTE: I live in Canada so my packaging is supposed to have English and French on it. The rule state because I am a small business I do not have to. But if you can figure a way to put in the design that would be fine but not necessary. If you did add it to the design it does not have to be the same size font as the English.
Should not have
• Pastel Colours.

```html
<!DOCTYPE html>
<html lang="en">
<head>
<meta charset="utf-8">
<title>Thistle &amp; Rye – Chicken Pot Pie Soup Label</title>
<link rel="stylesheet" href="https://fonts.googleapis.com/css2?family=Cinzel:wght@400;700&family=Cinzel+Decorative:wght@400&family=Josefin+Sans:wght@600&display=swap">
<style>
  :root {
    --paper: #dcc39f;
    --paper-light: #e2caa6;
    --grunge: #c89d6b;
    --ink: #0d0b09;
    --ornament: #3a3026;
    --hen-dark: #1b1815;
    --hen-mid: #4a4540;
  }
  * { box-sizing: border-box; margin: 0; padding: 0; }
  html, body { width: 999px; height: 1200px; overflow: hidden; background: var(--paper); }
  .label {
    position: relative;
    width: 999px;
    height: 1200px;
    overflow: hidden;
    color: var(--ink);
    background:
      radial-gradient(ellipse at 30% 30%, rgba(200,157,107,.5), transparent 55%),
      radial-gradient(ellipse at 72% 62%, rgba(200,157,107,.45), transparent 50%),
      var(--paper-light);
  }
  .frame, .hen-ring { position: absolute; left: 0; top: 0; }

  .ornament {
    position: absolute;
    width: 170px; height: 170px;
    background: var(--ornament);
    opacity: .35;
  }
  .ornament--tl { left: 18px; top: 18px; border-radius: 0 0 100% 0; }
  .ornament--tr { right: 18px; top: 18px; border-radius: 0 0 0 100%; }
  .ornament--bl { left: 18px; bottom: 18px; border-radius: 0 100% 0 0; }
  .ornament--br { right: 18px; bottom: 18px; border-radius: 100% 0 0 0; }

  .divider {
    position: absolute;
    left: 50%;
    transform: translateX(-50%);
    background: var(--ornament);
    opacity: .45;
    border-radius: 12px;
  }
  .divider--upper { top: 54px; width: 330px; height: 22px; }
  .divider--lower { top: 122px; width: 330px; height: 22px; }
  .divider--bottom { top: 984px; width: 620px; height: 24px; }

  .herb {
    position: absolute;
    background: var(--ornament);
    opacity: .55;
    border-radius: 50% 50% 50% 0;
  }
  .herb--left { left: 78px; top: 138px; width: 90px; height: 90px; }
  .herb--right { left: 832px; top: 142px; width: 70px; height: 80px; }

  .line-name {
    position: absolute; top: 84px; left: 0; width: 100%;
    text-align: center;
    font-family: "Josefin Sans", sans-serif;
    font-weight: 600;
    font-size: 28px;
    letter-spacing: 1px;
  }
  .motto {
    position: absolute; top: 160px; left: 0; width: 100%;
    text-align: center;
    font-family: "Cinzel", serif;
    font-weight: 700;
    font-size: 38px;
    line-height: 1;
  }
  .brand {
    position: absolute; top: 228px; left: 0; width: 100%;
    text-align: center;
    font-family: "Cinzel", serif;
    font-weight: 400;
    font-size: 70px;
    line-height: 1;
  }
  .product {
    position: absolute; left: 0; width: 100%;
    text-align: center;
    font-family: "Cinzel", serif;
    font-weight: 400;
    line-height: 1;
  }
  .product--line1 { top: 338px; font-size: 100px; }
  .product--line2 { top: 436px; font-size: 110px; }
  .product--line3 { top: 552px; font-size: 190px; font-family: "Cinzel Decorative", serif; }

  .hen-photo {
    position: absolute; left: 396px; top: 744px; width: 208px; height: 208px;
    border-radius: 50%;
    background: radial-gradient(circle at 45% 40%, var(--hen-mid), var(--hen-dark) 70%);
  }
  .french {
    position: absolute; top: 1028px; left: 0; width: 100%;
    text-align: center;
    font-family: "Cinzel", serif;
    font-size: 38px;
    line-height: 1;
  }
  .weight {
    position: absolute; top: 1096px; left: 0; width: 100%;
    text-align: center;
    font-family: "Cinzel", serif;
    font-size: 56px;
    line-height: 1;
  }
</style>
</head>
<body>
<main class="label">
  <svg class="frame" width="999" height="1200" viewBox="0 0 999 1200" aria-hidden="true">
    <rect x="16" y="16" width="967" height="1168" fill="none" stroke="var(--ink)" stroke-width="5"/>
    <rect x="28" y="28" width="943" height="1144" fill="none" stroke="var(--ink)" stroke-width="2"/>
    <line x1="76" y1="180" x2="76" y2="1030" stroke="var(--ink)" stroke-width="4"/>
    <line x1="923" y1="180" x2="923" y2="1030" stroke="var(--ink)" stroke-width="4"/>
    <line x1="200" y1="40" x2="799" y2="40" stroke="var(--ink)" stroke-width="3"/>
    <line x1="200" y1="1160" x2="799" y2="1160" stroke="var(--ink)" stroke-width="3"/>
  </svg>

  <div class="ornament ornament--tl" role="img" aria-label="Ornate vintage corner flourish"></div>
  <div class="ornament ornament--tr" role="img" aria-label="Ornate vintage corner flourish"></div>
  <div class="ornament ornament--bl" role="img" aria-label="Ornate vintage corner flourish"></div>
  <div class="ornament ornament--br" role="img" aria-label="Ornate vintage corner flourish"></div>

  <div class="divider divider--upper" role="img" aria-label="Decorative scroll divider"></div>
  <p class="line-name">UNCLE BARNABY'S</p>
  <div class="divider divider--lower" role="img" aria-label="Decorative scroll divider"></div>

  <div class="herb herb--left" role="img" aria-label="Herb sprig illustration"></div>
  <div class="herb herb--right" role="img" aria-label="Sage leaf illustration"></div>

  <p class="motto">Simple Suppers, Every Day</p>
  <h1 class="brand">Thistle &amp; Rye</h1>

  <h2 class="product product--line1">Chicken</h2>
  <h2 class="product product--line2">Pot Pie</h2>
  <h2 class="product product--line3">Soup</h2>

  <div class="hen-photo" role="img" aria-label="Photograph of a black hen"></div>
  <svg class="hen-ring" width="999" height="1200" viewBox="0 0 999 1200" aria-hidden="true">
    <circle cx="500" cy="848" r="116" fill="none" stroke="var(--ink)" stroke-width="8"/>
  </svg>

  <div class="divider divider--bottom" role="img" aria-label="Decorative scroll divider"></div>
  <p class="french">tarte au poulet Soupe</p>
  <p class="weight">150G.</p>
</main>
</body>
</html>
```